Bring us out of the Dark Ages!! Design a web submission form for our Intranet (HTML and CSS)

Good Day!
We are a small manufacturing company that after years of paper and manual processes is finally getting around to automating certain paper forms and tasks by using our Intranet site better.
One of the things we would like to automate is the "Annual Request for Vacation Time Off"
For the upcoming year, the company has calculated the number of vacations that can occur during each of the 52 weeks. In many cases, any given week in the year has multiple vacation slots available. (See Attachment 1 – Vacation Week Allocation).
This annual process allows all employees to submit a list of which vacation weeks they'd like to have in the order of their preference.
After all the submissions are collected, the weeks of vacation are awarded by company seniority.
We'd like to get some help with the design and coding of that Vacation Submission Form that will be deployed on our intranet site.
The employees will go to the submission form on the Intranet, select their desired week(s) of vacations, and then submit the form. The selections from the form should be entered into a database for processing later.
Because the weeks of vacation are awarded by company seniority, the form must accommodate employees submitting a multitude of choices to ensure they have a valid choice when their form is evaluated.
There is one more nuance to the process. Many employees have accrued more than one week of vacation and can submit for consecutive weeks. So the form not only needs to support a multitude of overall selections, but also a multitude of weeks as the person "spends" their vacation accrual.
Said a different way, I can choose any combination of weeks (consecutive or otherwise) for my annual vacation, but the number of weeks need to equal how many weeks I am eligible for. I also need to make enough of these "big" choices to provide for my seniority in the company.
We have included an idea that shows one possibility on how this form can work. (See Attachment 2 - Possible Form Flow). BUT PLEASE NOTE, IT DOES NOT HAVE TO BE THIS WAY...we want your creativity and ideas!!
Updates
Project Deadline Extended
Reason: All of the designs submitted are good, however they look like the mockup we submitted to explain the requirements. We specifically called out in our brief that we were also looking for designs that met our requirements of collecting the data but had a different user experience than the mockup we submitted.

```html
<!DOCTYPE html>
<html lang="en">
<head>
<meta charset="utf-8">
<title>Annual Request for Vacation Time Off</title>
<link rel="stylesheet" href="https://fonts.googleapis.com/css2?family=Roboto:wght@400;500;700&display=swap">
<style>
  :root {
    --page: #e4e6e7;
    --frame: #b9bec1;
    --panel: #2c343a;
    --ink-light: #e9ecee;
    --ink-dark: #222a2f;
    --field: #ffffff;
    --rule: #c9ced1;
    --dash: #aab2b7;
    --status: #c6cacc;
  }
  * { box-sizing: border-box; margin: 0; padding: 0; }
  html, body { width: 763px; height: 1200px; overflow: hidden; }
  body {
    background: var(--page);
    font-family: "Roboto", Arial, sans-serif;
    position: relative;
  }
  .window {
    position: absolute; left: 30px; top: 22px; width: 703px; height: 1156px;
    border: 2px solid var(--frame); background: var(--page);
  }
  .panel {
    position: absolute; left: 46px; top: 38px; width: 673px; height: 1082px;
    background: var(--panel);
  }
  .status-bar {
    position: absolute; left: 46px; top: 1128px; width: 673px; height: 32px;
    background: var(--status);
  }
  .form-title {
    position: absolute; left: 76px; top: 58px;
    color: var(--ink-light); font-weight: 700; font-size: 24px;
  }
  .title-rule {
    position: absolute; left: 76px; top: 97px; width: 612px; height: 2px;
    background: var(--rule);
  }
  .label {
    position: absolute; color: var(--ink-light); font-size: 14px; line-height: 22px;
  }
  .field {
    position: absolute; height: 22px; background: var(--field);
    color: var(--ink-dark); font-size: 13px; line-height: 22px; padding-left: 7px;
  }
  .field.select::after {
    content: ""; position: absolute; right: 8px; top: 8px;
    border-left: 5px solid transparent; border-right: 5px solid transparent;
    border-top: 6px solid var(--ink-dark);
  }
  .add {
    position: absolute; width: 22px; height: 22px; background: var(--field);
  }
  .add::before, .add::after {
    content: ""; position: absolute; background: var(--ink-dark);
  }
  .add::before { left: 5px; top: 10px; width: 12px; height: 2px; }
  .add::after { left: 10px; top: 5px; width: 2px; height: 12px; }
  .choice {
    position: absolute; border: 1.5px dashed var(--dash);
  }
  .choice-grip {
    position: absolute; right: 3px; bottom: 3px; width: 10px; height: 10px;
  }
  .choice-tab {
    position: absolute; height: 24px; padding: 0 14px; background: var(--field);
    color: var(--ink-dark); font-size: 13px; font-weight: 500; line-height: 24px;
  }
  .button {
    position: absolute; top: 1043px; height: 24px; background: var(--field);
    color: var(--ink-dark); font-size: 14px; line-height: 24px; text-align: center;
  }
</style>
</head>
<body>
  <div class="window"></div>
  <main class="panel"></main>
  <div class="status-bar"></div>

  <h1 class="form-title">Annual Request for Vacation Time Off</h1>
  <div class="title-rule"></div>

  <!-- Employee details -->
  <span class="label" style="left:76px;top:134px">Employee ID</span>
  <div class="field" style="left:262px;top:134px;width:125px">11469</div>

  <span class="label" style="left:76px;top:180px">Employment Type</span>
  <div class="field select" style="left:262px;top:180px;width:188px">Engineer</div>

  <span class="label" style="left:76px;top:226px">Department</span>
  <div class="field select" style="left:262px;top:226px;width:188px">Software</div>

  <span class="label" style="left:76px;top:272px">Designation</span>
  <div class="field" style="left:262px;top:272px;width:183px">Sr. Software Engineer</div>

  <!-- Choice group 1 -->
  <section class="choice" style="left:97px;top:378px;width:412px;height:150px">
    <svg class="choice-grip" viewBox="0 0 10 10"><path d="M2 10 L10 2 M6 10 L10 6" stroke="#aab2b7" stroke-width="1"/></svg>
  </section>
  <div class="choice-tab" style="left:107px;top:364px">Chose 01</div>
  <div class="add" style="left:214px;top:365px"></div>
  <span class="label" style="left:132px;top:420px">Fiscal Year</span>
  <div class="field select" style="left:262px;top:420px;width:160px">2015-2016</div>
  <div class="add" style="left:438px;top:420px"></div>
  <span class="label" style="left:132px;top:461px">Month</span>
  <div class="field select" style="left:262px;top:461px;width:160px">December</div>
  <div class="add" style="left:438px;top:461px"></div>
  <span class="label" style="left:132px;top:498px">Block #1</span>
  <div class="add" style="left:225px;top:498px"></div>
  <div class="field select" style="left:262px;top:498px;width:160px">Week 21</div>
  <div class="add" style="left:438px;top:498px"></div>

  <!-- Choice group 2 -->
  <section class="choice" style="left:97px;top:567px;width:584px;height:173px">
    <svg class="choice-grip" viewBox="0 0 10 10"><path d="M2 10 L10 2 M6 10 L10 6" stroke="#aab2b7" stroke-width="1"/></svg>
  </section>
  <div class="choice-tab" style="left:107px;top:553px">Chose 01</div>
  <div class="add" style="left:214px;top:554px"></div>
  <span class="label" style="left:132px;top:602px">Fiscal Year</span>
  <div class="field select" style="left:262px;top:602px;width:160px">2015-2016</div>
  <div class="add" style="left:438px;top:602px"></div>
  <div class="field select" style="left:496px;top:602px;width:163px">2016-2017</div>
  <span class="label" style="left:132px;top:645px">Month</span>
  <div class="field select" style="left:262px;top:645px;width:160px">December</div>
  <div class="add" style="left:438px;top:645px"></div>
  <div class="field select" style="left:496px;top:645px;width:163px">November</div>
  <span class="label" style="left:132px;top:686px">Block #1</span>
  <div class="add" style="left:225px;top:686px"></div>
  <div class="field select" style="left:262px;top:686px;width:160px">Week 21</div>
  <div class="add" style="left:438px;top:686px"></div>
  <div class="field select" style="left:496px;top:686px;width:163px">Week 22</div>

  <!-- Choice group 3 -->
  <section class="choice" style="left:97px;top:797px;width:584px;height:216px">
    <svg class="choice-grip" viewBox="0 0 10 10"><path d="M2 10 L10 2 M6 10 L10 6" stroke="#aab2b7" stroke-width="1"/></svg>
  </section>
  <div class="choice-tab" style="left:107px;top:783px">Chose 02</div>
  <div class="add" style="left:214px;top:784px"></div>
  <span class="label" style="left:132px;top:831px">Fiscal Year</span>
  <div class="field select" style="left:262px;top:831px;width:160px">2015-2016</div>
  <div class="add" style="left:438px;top:831px"></div>
  <div class="field select" style="left:496px;top:831px;width:163px">2016-2017</div>
  <span class="label" style="left:132px;top:872px">Month</span>
  <div class="field select" style="left:262px;top:872px;width:160px">December</div>
  <div class="add" style="left:438px;top:872px"></div>
  <div class="field select" style="left:496px;top:872px;width:163px">November</div>
  <span class="label" style="left:132px;top:913px">Block #1</span>
  <div class="add" style="left:225px;top:913px"></div>
  <div class="field select" style="left:262px;top:913px;width:160px">Week 21</div>
  <div class="add" style="left:438px;top:913px"></div>
  <div class="field select" style="left:496px;top:913px;width:163px">Week 22</div>
  <span class="label" style="left:132px;top:954px">Block #2</span>
  <div class="add" style="left:225px;top:954px"></div>
  <div class="field select" style="left:262px;top:954px;width:160px">Week 23</div>
  <div class="add" style="left:438px;top:954px"></div>
  <div class="field select" style="left:496px;top:954px;width:163px">Week 24</div>

  <!-- Actions -->
  <div class="button" style="left:498px;width:82px">Submit</div>
  <div class="button" style="left:600px;width:81px">Reset</div>
</body>
</html>
```